Chocolate Packaging in IT Style (Corporate Design: velmora)

We are looking for a modern, eye-catching wrapper design for our promotional chocolate bar, which will be handed out to clients and partners.
The design should visually reflect our corporate identity, with elements such as:
- Dark background (black or dark gray)
- Colorful accents like lines, data points, or tech-inspired details
Please take inspiration from our website: www.velmora-it.example
Logo: Our velmora IT-Services logo must be clearly visible and well-integrated.
Optional text: You may include a short slogan (eg, “IT performance you can taste” or “Fuel your IT – with flavor”).
Important:
The "Brunik" logo is mandatory, but can be recolored.
Please always save with a 3 mm bleed.
Hide the punch and do not save with the print file.
Print information:
Print file: PDF
Resolution: print quality with a minimum resolution of 300dpi
Type: if possible, create outlines
Color mode: print files have to be in CMYK, ie 4C color mode or grayscale. Anything deviating from this standard will lead to color discrepancies in the printed product.
Because white is very susceptible to dirt, please do not use a white envelope.
Data format/bleed: 3mm added bleed including crop lines
Punch: hide or edit out the punch, if it's visible, and don't save it with the print file.
Look and feel
Each slider illustrates characteristics of the customer's brand and the style your logo design should communicate.

```html
<!DOCTYPE html>
<html lang="en">
<head>
<meta charset="utf-8">
<title>velmora – Brunik Classic chocolate wrapper</title>
<link href="https://fonts.googleapis.com/css2?family=Montserrat:wght@600;800&family=Kaushan+Script&family=Gilda+Display&family=VT323&family=Press+Start+2P&display=swap" rel="stylesheet">
<style>
  :root{
    --page:#ffffff;
    --wrapper:#2f3e4a;
    --band:#14191e;
    --accent:#2fa1dc;
    --flavor:#f2c21b;
    --panel:#52646f;
    --logo-ink:#1f3a78;
    --code-bg:#111417;
    --code-ink:#ffffff;
    --binary:#4f6270;
  }
  html,body{margin:0;padding:0;width:1200px;height:959px;overflow:hidden;background:var(--page);}
  .wrapper{position:absolute;left:374px;top:40px;width:452px;height:880px;background:var(--wrapper);overflow:hidden;}
  .brand-band{position:absolute;left:0;top:43px;width:452px;height:35px;background:var(--band);}
  .brand-name{position:absolute;left:0;width:100%;top:0;line-height:35px;text-align:center;margin:0;
    font-family:"Montserrat",sans-serif;font-weight:800;font-size:24px;color:var(--accent);
    letter-spacing:38px;text-indent:38px;text-transform:lowercase;}
  .line-name{position:absolute;left:0;width:100%;top:82px;text-align:center;margin:0;
    font-family:"Gilda Display",serif;font-size:46px;color:var(--accent);letter-spacing:28px;text-indent:22px;}
  .logo-card{position:absolute;left:0;top:175px;width:240px;height:108px;background:#fff;
    display:flex;align-items:center;justify-content:center;gap:8px;}
  .logo-card .mark{width:14px;height:14px;background:var(--logo-ink);}
  .logo-card .name{font-family:"Montserrat",sans-serif;font-weight:600;font-size:36px;color:var(--logo-ink);letter-spacing:1px;}
  .slogan{position:absolute;left:40px;top:318px;margin:0;font-family:"Montserrat",sans-serif;font-weight:800;
    font-size:55px;line-height:1;color:var(--accent);letter-spacing:-0.5px;}
  .slogan-sub{position:absolute;left:68px;top:368px;margin:0;font-family:"Kaushan Script",cursive;
    font-size:44px;color:var(--flavor);transform:rotate(-4deg);transform-origin:left center;}
  .binary{position:absolute;font-family:"Courier New",monospace;font-size:8px;line-height:14px;color:var(--binary);white-space:pre;margin:0;}
  .binary.top{left:54px;top:418px;}
  .binary.side{left:92px;top:460px;}
  .binary.bottom{left:4px;top:795px;}
  .screen{position:absolute;left:138px;top:479px;width:273px;height:325px;background:var(--panel);
    border:2px solid var(--accent);border-top:13px solid var(--accent);box-sizing:border-box;}
  .pointing-hand{position:absolute;left:38px;top:492px;width:414px;height:205px;border-radius:40px 0 0 40px;
    background:linear-gradient(100deg,rgba(47,161,220,.55),rgba(47,161,220,.9));}
  .dialog{position:absolute;left:68px;top:654px;width:226px;height:111px;box-sizing:border-box;
    background:var(--code-bg);border:3px solid var(--accent);outline:2px solid var(--code-bg);outline-offset:-7px;padding:9px 12px;}
  .dialog pre{margin:0;font-family:"VT323",monospace;font-size:11px;line-height:9px;color:var(--code-ink);}
  .dialog .choice{margin-top:12px;font-family:"Press Start 2P",monospace;font-size:11px;color:var(--code-ink);word-spacing:6px;}
  .dialog-tail{position:absolute;left:245px;top:762px;}
</style>
</head>
<body>
<div class="wrapper">
  <div class="brand-band"><p class="brand-name">brunik</p></div>
  <p class="line-name">Classic</p>

  <div class="logo-card"><span class="mark"></span><span class="name">velmora</span></div>

  <h1 class="slogan">Fuel your IT</h1>
  <p class="slogan-sub">with flavor</p>

  <pre class="binary top">111001     1010010110100  000000110010001101110110111001000
110101     0111010000101  000010000001100011011011110110
000100     00000101100100  11010010111000001101001011100</pre>
  <pre class="binary side">001011
001000
000111
111010
000101
001100
101100
101011</pre>
  <pre class="binary bottom">1010010111       0000
1000110000       10011011111011100100111 0        110100101110</pre>

  <div class="screen"></div>
  <div class="pointing-hand" role="img" aria-label="Blue wireframe hand pointing to the left"></div>

  <div class="dialog">
<pre>W[1] =
np.random.zeros
 loss =
0.6931471805599453
accuracy = 50 %</pre>
    <div class="choice">Yes/ No</div>
  </div>
  <svg class="dialog-tail" width="34" height="26" viewBox="0 0 34 26" aria-hidden="true">
    <polygon points="2,0 32,0 32,24" fill="var(--code-bg)" stroke="var(--accent)" stroke-width="3"/>
  </svg>
</div>
</body>
</html>
```